Etiketten-Design für Brause in der Flasche gesucht
Zielgruppe
Wir sind eine kleine Brauerei. Wir haben hier schon unsere Bieretiketten designen lassen.
Aufgabenstellung
Nun suchen wir Etiketten für 0,33l Falschen für unsere Brause...Momentan haben wir z.B. Rharbarber gemacht.
Es werden aber noch noch andere gemacht..also evtl ein Design das man den verschiedenen Früchten anpassen kann.
Unser Logo vom Hof sollte mit eingebaut werden.

```html
<!DOCTYPE html>
<html lang="de">
<head>
<meta charset="utf-8">
<title>Brause Etiketten – Hof Lindenau</title>
<link rel="stylesheet" href="https://fonts.googleapis.com/css2?family=Sacramento&family=Yellowtail&family=Source+Sans+3:wght@600;700&display=swap">
<style>
  :root {
    --forest: #2a5c47;
    --gold: #f2bb1b;
    --white: #ffffff;
    --paper: #ffffff;
    --rhubarb: #f4677a;
    --rhubarb-accent: #f9a59c;
    --lime: #9ad337;
    --lime-accent: #c8f08e;
    --elder: #7b8ff7;
    --elder-accent: #b3c0ff;
    --passion: #fbae17;
    --passion-accent: #fdd28e;
  }
  html, body {
    margin: 0;
    padding: 0;
    width: 946px;
    height: 1200px;
    overflow: hidden;
    background: var(--paper);
  }
  .sheet {
    position: relative;
    width: 946px;
    height: 1200px;
  }
  .label {
    position: absolute;
    width: 384px;
    height: 521px;
    box-sizing: border-box;
    border: 4px solid var(--forest);
    background: var(--fill);
    overflow: hidden;
  }
  .label--rhubarb { left: 50px;  top: 47px;  --fill: var(--rhubarb); --accent: var(--rhubarb-accent); }
  .label--lime    { left: 506px; top: 47px;  --fill: var(--lime);    --accent: var(--lime-accent); }
  .label--elder   { left: 50px;  top: 618px; --fill: var(--elder);   --accent: var(--elder-accent); }
  .label--passion { left: 506px; top: 618px; --fill: var(--passion); --accent: var(--passion-accent); }

  .label__frame {
    position: absolute;
    inset: 7px;
    border: 2px solid var(--white);
    z-index: 3;
    pointer-events: none;
  }
  .label__foliage {
    position: absolute;
    width: 130px;
    height: 130px;
    z-index: 1;
    background: radial-gradient(circle at var(--pos), rgba(255,255,255,0.55) 0%, rgba(255,255,255,0.18) 45%, rgba(255,255,255,0) 72%);
  }
  .label__foliage--tl { left: 0; top: 0; --pos: 0% 0%; }
  .label__foliage--tr { right: 0; top: 0; --pos: 100% 0%; }
  .label__foliage--ml { left: 0; top: 300px; --pos: 0% 60%; }
  .label__foliage--mr { right: 0; top: 290px; --pos: 100% 50%; }
  .label__foliage--bl { left: 0; bottom: 0; --pos: 0% 100%; }
  .label__foliage--br { right: 0; bottom: 0; --pos: 100% 100%; }
  .label__foliage--band { right: 0; top: 160px; width: 80px; height: 110px; --pos: 100% 50%; }

  .label__band {
    position: absolute;
    left: 0;
    right: 0;
    top: 170px;
    height: 134px;
    background: var(--forest);
    z-index: 0;
  }
  .label__flavour {
    position: absolute;
    left: 0;
    right: 0;
    top: 66px;
    margin: 0;
    text-align: center;
    font-family: "Sacramento", cursive;
    font-weight: 400;
    font-size: 62px;
    line-height: 1;
    color: var(--white);
    z-index: 2;
  }
  .label__product {
    position: absolute;
    left: 0;
    right: 0;
    top: 176px;
    margin: 0;
    text-align: center;
    font-family: "Yellowtail", cursive;
    font-weight: 400;
    font-size: 104px;
    line-height: 1.1;
    color: var(--gold);
    z-index: 2;
  }
  .label__bubbles {
    position: absolute;
    inset: 0;
    z-index: 2;
  }
  .bubble--ring { fill: none; stroke: var(--white); stroke-width: 2.5; }
  .bubble--dot { fill: var(--white); }
  .bubble--accent { fill: var(--accent); stroke: var(--white); stroke-width: 1.5; }
  .bubble--gold { fill: var(--gold); }

  .label__brand {
    position: absolute;
    left: 0;
    right: 0;
    top: 330px;
    text-align: center;
    z-index: 2;
    color: var(--forest);
  }
  .brand__mark {
    display: block;
    width: 62px;
    height: 62px;
    margin: 0 auto 12px;
    border: 4px solid var(--forest);
    border-radius: 50%;
    box-sizing: border-box;
  }
  .brand__name {
    display: block;
    font-family: "Source Sans 3", sans-serif;
    font-weight: 700;
    font-size: 36px;
    line-height: 1;
    letter-spacing: 0.2px;
  }
  .brand__place {
    display: block;
    margin-top: 8px;
    font-family: "Source Sans 3", sans-serif;
    font-weight: 600;
    font-size: 19px;
    letter-spacing: 4px;
  }
</style>
</head>
<body>
<main class="sheet">

  <section class="label label--rhubarb">
    <div class="label__band"></div>
    <div class="label__foliage label__foliage--tl" role="img" aria-label="Weiße Blattranken"></div>
    <div class="label__foliage label__foliage--tr" role="img" aria-label="Weiße Blattranken"></div>
    <div class="label__foliage label__foliage--band" role="img" aria-label="Weiße Blattranken"></div>
    <div class="label__foliage label__foliage--ml" role="img" aria-label="Weiße Blattranken"></div>
    <div class="label__foliage label__foliage--mr" role="img" aria-label="Weiße Blattranken"></div>
    <div class="label__foliage label__foliage--bl" role="img" aria-label="Weiße Blattranken"></div>
    <div class="label__foliage label__foliage--br" role="img" aria-label="Weiße Blattranken"></div>
    <h2 class="label__flavour">Rhabarber</h2>
    <h1 class="label__product">Brause</h1>
    <svg class="label__bubbles" viewBox="0 0 384 521" aria-hidden="true">
      <circle class="bubble--dot" cx="40" cy="141" r="4"/>
      <circle class="bubble--ring" cx="50" cy="163" r="6"/>
      <circle class="bubble--dot" cx="90" cy="150" r="3"/>
      <circle class="bubble--ring" cx="118" cy="165" r="6"/>
      <circle class="bubble--dot" cx="172" cy="158" r="4"/>
      <circle class="bubble--accent" cx="222" cy="149" r="9"/>
      <circle class="bubble--ring" cx="275" cy="146" r="6"/>
      <circle class="bubble--ring" cx="206" cy="193" r="6"/>
      <circle class="bubble--accent" cx="270" cy="192" r="8"/>
      <circle class="bubble--ring" cx="234" cy="186" r="5"/>
      <circle class="bubble--accent" cx="26" cy="260" r="9"/>
      <circle class="bubble--ring" cx="182" cy="283" r="10"/>
      <circle class="bubble--dot" cx="148" cy="287" r="4"/>
      <circle class="bubble--dot" cx="240" cy="274" r="4"/>
      <circle class="bubble--ring" cx="260" cy="260" r="6"/>
      <circle class="bubble--gold" cx="322" cy="284" r="6"/>
      <circle class="bubble--accent" cx="122" cy="302" r="8"/>
      <circle class="bubble--ring" cx="228" cy="311" r="6"/>
      <circle class="bubble--ring" cx="44" cy="322" r="7"/>
      <circle class="bubble--dot" cx="258" cy="345" r="4"/>
    </svg>
    <div class="label__brand">
      <span class="brand__mark"></span>
      <span class="brand__name">Hof Lindenau</span>
      <span class="brand__place">WENDORF</span>
    </div>
    <div class="label__frame"></div>
  </section>

  <section class="label label--lime">
    <div class="label__band"></div>
    <div class="label__foliage label__foliage--tl" role="img" aria-label="Weiße Blattranken"></div>
    <div class="label__foliage label__foliage--tr" role="img" aria-label="Weiße Blattranken"></div>
    <div class="label__foliage label__foliage--band" role="img" aria-label="Weiße Blattranken"></div>
    <div class="label__foliage label__foliage--ml" role="img" aria-label="Weiße Blattranken"></div>
    <div class="label__foliage label__foliage--mr" role="img" aria-label="Weiße Blattranken"></div>
    <div class="label__foliage label__foliage--bl" role="img" aria-label="Weiße Blattranken"></div>
    <div class="label__foliage label__foliage--br" role="img" aria-label="Weiße Blattranken"></div>
    <h2 class="label__flavour">Limetten</h2>
    <h1 class="label__product">Brause</h1>
    <svg class="label__bubbles" viewBox="0 0 384 521" aria-hidden="true">
      <circle class="bubble--dot" cx="40" cy="141" r="4"/>
      <circle class="bubble--ring" cx="50" cy="163" r="6"/>
      <circle class="bubble--dot" cx="90" cy="150" r="3"/>
      <circle class="bubble--ring" cx="118" cy="165" r="6"/>
      <circle class="bubble--dot" cx="172" cy="158" r="4"/>
      <circle class="bubble--accent" cx="222" cy="149" r="9"/>
      <circle class="bubble--ring" cx="275" cy="146" r="6"/>
      <circle class="bubble--ring" cx="206" cy="193" r="6"/>
      <circle class="bubble--accent" cx="270" cy="192" r="8"/>
      <circle class="bubble--ring" cx="234" cy="186" r="5"/>
      <circle class="bubble--accent" cx="26" cy="260" r="9"/>
      <circle class="bubble--ring" cx="182" cy="283" r="10"/>
      <circle class="bubble--dot" cx="148" cy="287" r="4"/>
      <circle class="bubble--dot" cx="240" cy="274" r="4"/>
      <circle class="bubble--ring" cx="260" cy="260" r="6"/>
      <circle class="bubble--gold" cx="322" cy="284" r="6"/>
      <circle class="bubble--accent" cx="122" cy="302" r="8"/>
      <circle class="bubble--ring" cx="228" cy="311" r="6"/>
      <circle class="bubble--ring" cx="44" cy="322" r="7"/>
      <circle class="bubble--dot" cx="258" cy="345" r="4"/>
    </svg>
    <div class="label__brand">
      <span class="brand__mark"></span>
      <span class="brand__name">Hof Lindenau</span>
      <span class="brand__place">WENDORF</span>
    </div>
    <div class="label__frame"></div>
  </section>

  <section class="label label--elder">
    <div class="label__band"></div>
    <div class="label__foliage label__foliage--tl" role="img" aria-label="Weiße Blattranken"></div>
    <div class="label__foliage label__foliage--tr" role="img" aria-label="Weiße Blattranken"></div>
    <div class="label__foliage label__foliage--band" role="img" aria-label="Weiße Blattranken"></div>
    <div class="label__foliage label__foliage--ml" role="img" aria-label="Weiße Blattranken"></div>
    <div class="label__foliage label__foliage--mr" role="img" aria-label="Weiße Blattranken"></div>
    <div class="label__foliage label__foliage--bl" role="img" aria-label="Weiße Blattranken"></div>
    <div class="label__foliage label__foliage--br" role="img" aria-label="Weiße Blattranken"></div>
    <h2 class="label__flavour">Hollunder</h2>
    <h1 class="label__product">Brause</h1>
    <svg class="label__bubbles" viewBox="0 0 384 521" aria-hidden="true">
      <circle class="bubble--dot" cx="40" cy="141" r="4"/>
      <circle class="bubble--ring" cx="50" cy="163" r="6"/>
      <circle class="bubble--dot" cx="90" cy="150" r="3"/>
      <circle class="bubble--ring" cx="118" cy="165" r="6"/>
      <circle class="bubble--dot" cx="172" cy="158" r="4"/>
      <circle class="bubble--accent" cx="222" cy="149" r="9"/>
      <circle class="bubble--ring" cx="275" cy="146" r="6"/>
      <circle class="bubble--ring" cx="206" cy="193" r="6"/>
      <circle class="bubble--accent" cx="270" cy="192" r="8"/>
      <circle class="bubble--ring" cx="234" cy="186" r="5"/>
      <circle class="bubble--accent" cx="26" cy="260" r="9"/>
      <circle class="bubble--ring" cx="182" cy="283" r="10"/>
      <circle class="bubble--dot" cx="148" cy="287" r="4"/>
      <circle class="bubble--dot" cx="240" cy="274" r="4"/>
      <circle class="bubble--ring" cx="260" cy="260" r="6"/>
      <circle class="bubble--gold" cx="322" cy="284" r="6"/>
      <circle class="bubble--accent" cx="122" cy="302" r="8"/>
      <circle class="bubble--ring" cx="228" cy="311" r="6"/>
      <circle class="bubble--ring" cx="44" cy="322" r="7"/>
      <circle class="bubble--dot" cx="258" cy="345" r="4"/>
    </svg>
    <div class="label__brand">
      <span class="brand__mark"></span>
      <span class="brand__name">Hof Lindenau</span>
      <span class="brand__place">WENDORF</span>
    </div>
    <div class="label__frame"></div>
  </section>

  <section class="label label--passion">
    <div class="label__band"></div>
    <div class="label__foliage label__foliage--tl" role="img" aria-label="Weiße Blattranken"></div>
    <div class="label__foliage label__foliage--tr" role="img" aria-label="Weiße Blattranken"></div>
    <div class="label__foliage label__foliage--band" role="img" aria-label="Weiße Blattranken"></div>
    <div class="label__foliage label__foliage--ml" role="img" aria-label="Weiße Blattranken"></div>
    <div class="label__foliage label__foliage--mr" role="img" aria-label="Weiße Blattranken"></div>
    <div class="label__foliage label__foliage--bl" role="img" aria-label="Weiße Blattranken"></div>
    <div class="label__foliage label__foliage--br" role="img" aria-label="Weiße Blattranken"></div>
    <h2 class="label__flavour">Maracuya</h2>
    <h1 class="label__product">Brause</h1>
    <svg class="label__bubbles" viewBox="0 0 384 521" aria-hidden="true">
      <circle class="bubble--dot" cx="40" cy="141" r="4"/>
      <circle class="bubble--ring" cx="50" cy="163" r="6"/>
      <circle class="bubble--dot" cx="90" cy="150" r="3"/>
      <circle class="bubble--ring" cx="118" cy="165" r="6"/>
      <circle class="bubble--dot" cx="172" cy="158" r="4"/>
      <circle class="bubble--accent" cx="222" cy="149" r="9"/>
      <circle class="bubble--ring" cx="275" cy="146" r="6"/>
      <circle class="bubble--ring" cx="206" cy="193" r="6"/>
      <circle class="bubble--accent" cx="270" cy="192" r="8"/>
      <circle class="bubble--ring" cx="234" cy="186" r="5"/>
      <circle class="bubble--accent" cx="26" cy="260" r="9"/>
      <circle class="bubble--ring" cx="182" cy="283" r="10"/>
      <circle class="bubble--dot" cx="148" cy="287" r="4"/>
      <circle class="bubble--dot" cx="240" cy="274" r="4"/>
      <circle class="bubble--ring" cx="260" cy="260" r="6"/>
      <circle class="bubble--gold" cx="322" cy="284" r="6"/>
      <circle class="bubble--accent" cx="122" cy="302" r="8"/>
      <circle class="bubble--ring" cx="228" cy="311" r="6"/>
      <circle class="bubble--ring" cx="44" cy="322" r="7"/>
      <circle class="bubble--dot" cx="258" cy="345" r="4"/>
    </svg>
    <div class="label__brand">
      <span class="brand__mark"></span>
      <span class="brand__name">Hof Lindenau</span>
      <span class="brand__place">WENDORF</span>
    </div>
    <div class="label__frame"></div>
  </section>

</main>
</body>
</html>
```